Business Card for a Wedding Films Business

We require a business card design for our business 'Lewis Barnow Wedding Films'. The logo needs to look classy and high end.

Target Market(s)

Wedding Couples

Contact Information for Business Card

Lewis Barnow Wedding Films
07312 580 417
films@lewisbarnow-example.com
www.lewisbarnow-example.com

Facebook: @lewisbarnowweddingfilms
Instagram: @lewisbarnowfilms

Font styles to use
Sans Serif

Requirements
Must have
• Social media icons - Facebook and Instagram

```html
<!DOCTYPE html>
<html lang="en">
<head>
<meta charset="utf-8">
<title>Lewis Barnow Wedding Films – Business Card</title>
<link rel="stylesheet" href="https://fonts.googleapis.com/css2?family=Jost:wght@400;500&display=swap">
<style>
  :root {
    --stage: #3a3a3a;
    --card-light: #ffffff;
    --card-dark: #1c1c1c;
    --ink: #111111;
    --ink-reverse: #ffffff;
    --ink-soft: #2a2a2a;
  }
  * { box-sizing: border-box; margin: 0; padding: 0; }
  html, body { width: 1200px; height: 900px; overflow: hidden; }
  body {
    background: radial-gradient(ellipse at 50% 45%, #4a4a4a 0%, var(--stage) 70%);
    font-family: "Jost", sans-serif;
    position: relative;
  }
  .card {
    position: absolute;
    top: 150px;
    width: 340px;
    height: 595px;
    box-shadow: 0 18px 40px rgba(0,0,0,0.45);
  }
  .card--front { left: 230px; background: var(--card-light); color: var(--ink); }
  .card--back { left: 630px; background: var(--card-dark); color: var(--ink-reverse); }

  .brand {
    position: absolute;
    left: 0; right: 0;
    display: flex;
    flex-direction: column;
    align-items: center;
  }
  .card--front .brand { top: 80px; }
  .card--back .brand { top: 50%; transform: translateY(-50%); }
  .brand__mark {
    width: 34px; height: 34px;
    border: 2px solid currentColor;
    margin-bottom: 12px;
  }
  .brand__name {
    font-weight: 500;
    font-size: 19px;
    letter-spacing: 4px;
    text-transform: uppercase;
    line-height: 1.2;
    white-space: nowrap;
  }
  .brand__tag {
    font-weight: 500;
    font-size: 10px;
    letter-spacing: 5px;
    text-transform: uppercase;
    margin-top: 3px;
    white-space: nowrap;
  }

  .person {
    position: absolute;
    top: 300px; left: 0; right: 0;
    text-align: center;
  }
  .person__name { font-size: 24px; font-weight: 500; letter-spacing: 1px; text-transform: uppercase; line-height: 1.2; }
  .person__role { font-size: 14px; color: var(--ink-soft); margin-top: 2px; }

  .icon-row {
    display: flex; justify-content: center; align-items: center; gap: 8px;
    margin: 12px 0 6px;
  }
  .icon-row svg { width: 12px; height: 12px; display: block; }

  .contact {
    position: absolute;
    top: 360px; left: 0; right: 0;
    text-align: center;
    font-size: 15.5px;
    line-height: 1.35;
  }
  .contact__line { display: block; white-space: nowrap; }
</style>
</head>
<body>

  <section class="card card--front" aria-label="Business card front">
    <div class="brand">
      <div class="brand__mark"></div>
      <div class="brand__name">Lewis Barnow</div>
      <div class="brand__tag">Wedding Films</div>
    </div>

    <div class="person">
      <div class="person__name">Daniel Hart</div>
      <div class="person__role">Director</div>
    </div>

    <div class="contact">
      <div class="contact__group">
        <div class="icon-row">
          <svg viewBox="0 0 12 12" role="img" aria-label="Social page icon"><rect x="1" y="1" width="10" height="10" rx="2" fill="#111"/></svg>
          <svg viewBox="0 0 12 12" role="img" aria-label="Photo profile icon"><rect x="1.3" y="1.3" width="9.4" height="9.4" rx="2.5" fill="none" stroke="#111" stroke-width="1.4"/></svg>
        </div>
        <span class="contact__line">/lewisbarnowweddingfilms</span>
        <span class="contact__line">@lewisbarnowfilms</span>
      </div>
      <div class="contact__group">
        <div class="icon-row">
          <svg viewBox="0 0 12 12" aria-hidden="true"><path d="M2.5 1h2l1 3-1.3.9a6 6 0 0 0 2.9 2.9L8 6.5l3 1v2c0 .8-.7 1.5-1.5 1.5A8.5 8.5 0 0 1 1 2.5C1 1.7 1.7 1 2.5 1z" fill="#111"/></svg>
          <svg viewBox="0 0 12 12" aria-hidden="true"><rect x="0.8" y="2.3" width="10.4" height="7.4" fill="none" stroke="#111" stroke-width="1.2"/><path d="M1 2.6 6 6.6l5-4" fill="none" stroke="#111" stroke-width="1.2"/></svg>
          <svg viewBox="0 0 12 12" aria-hidden="true"><circle cx="6" cy="6" r="5" fill="none" stroke="#111" stroke-width="1.1"/><ellipse cx="6" cy="6" rx="2.2" ry="5" fill="none" stroke="#111" stroke-width="1"/><path d="M1 6h10M2 3.5h8M2 8.5h8" stroke="#111" stroke-width="0.9"/></svg>
        </div>
        <span class="contact__line">07312 580 417</span>
        <span class="contact__line">films@lewisbarnow-example.com</span>
        <span class="contact__line">www.lewisbarnow-example.com</span>
      </div>
    </div>
  </section>

  <section class="card card--back" aria-label="Business card back">
    <div class="brand">
      <div class="brand__mark"></div>
      <div class="brand__name">Lewis Barnow</div>
      <div class="brand__tag">Wedding Films</div>
    </div>
  </section>

</body>
</html>
```